Business card and stationary design for construction company
RT Garland Construction
Business card and stationary design for construction company - Construction
Creative Brief
Professional
Marcus Garland
President
781 Willow Bend Dr Maple Hollow, OR 97999
marcus@rt-garland.example
rt-garland.example

```html
<!DOCTYPE html>
<html lang="en">
<head>
<meta charset="utf-8">
<title>RT Garland Construction – Business Card</title>
<link href="https://fonts.googleapis.com/css2?family=Open+Sans:wght@400;600;700&display=swap" rel="stylesheet">
<style>
  :root {
    --backdrop: #e6e7e9;
    --card-white: #ffffff;
    --brand-blue: #2b78b4;
    --brand-blue-light: #3a8ac6;
    --brand-blue-deep: #1f5f94;
    --logo-navy: #1d4f86;
    --text-white: #ffffff;
    --text-soft: #e3eef8;
  }
  * { margin: 0; padding: 0; box-sizing: border-box; }
  html, body {
    width: 1200px; height: 900px; overflow: hidden;
    background: var(--backdrop);
    font-family: "Open Sans", Arial, sans-serif;
  }
  .canvas {
    width: 1200px; height: 900px;
    display: flex; align-items: center; justify-content: center;
  }
  .business-card {
    position: relative;
    width: 1000px; height: 572px;
    background: var(--card-white);
    box-shadow: 0 18px 40px rgba(0,0,0,0.18);
    overflow: hidden;
  }
  .brand-lockup {
    position: absolute; top: 0; left: 0; right: 0; height: 230px;
    display: flex; align-items: center; justify-content: center; gap: 16px;
  }
  .brand-square {
    width: 44px; height: 44px; background: var(--logo-navy);
  }
  .brand-name {
    font-weight: 700; font-size: 38px; color: var(--logo-navy);
    letter-spacing: 0.5px;
  }
  .blue-panel {
    position: absolute; left: 0; right: 0; top: 230px; bottom: 0;
    background: var(--brand-blue);
  }
  .panel-highlight {
    position: absolute; left: 0; right: 0; top: 0; height: 16px;
    background: var(--brand-blue-light);
  }
  .panel-base {
    position: absolute; left: 0; right: 0; bottom: 0; height: 44px;
    background: var(--brand-blue-deep);
  }
  .person {
    position: absolute; left: 64px; top: 330px; color: var(--text-white);
  }
  .person-name { font-weight: 700; font-size: 34px; line-height: 1.2; }
  .person-title { font-weight: 400; font-size: 27px; color: var(--text-soft); margin-top: 4px; }
  .contact-list {
    position: absolute; left: 640px; top: 258px;
    list-style: none; color: var(--text-white);
    font-size: 19px; line-height: 1.3;
  }
  .contact-item { display: flex; align-items: flex-start; gap: 12px; margin-bottom: 10px; }
  .contact-icon { flex: 0 0 24px; width: 24px; height: 24px; margin-top: 1px; }
</style>
</head>
<body>
<main class="canvas">
  <article class="business-card">
    <header class="brand-lockup">
      <span class="brand-square"></span>
      <span class="brand-name">RT Garland Construction</span>
    </header>

    <section class="blue-panel">
      <div class="panel-highlight"></div>
      <div class="panel-base"></div>
    </section>

    <div class="person">
      <p class="person-name">Marcus Garland</p>
      <p class="person-title">President</p>
    </div>

    <ul class="contact-list">
      <li class="contact-item">
        <svg class="contact-icon" viewBox="0 0 24 24"><circle cx="12" cy="12" r="12" fill="#fff"/><path d="M12 5a4.5 4.5 0 0 0-4.5 4.5c0 3.3 4.5 9 4.5 9s4.5-5.7 4.5-9A4.5 4.5 0 0 0 12 5zm0 6.2a1.7 1.7 0 1 1 0-3.4 1.7 1.7 0 0 1 0 3.4z" fill="#2b78b4"/></svg>
        <span>781 Willow Bend Dr<br>Maple Hollow, OR<br>97999</span>
      </li>
      <li class="contact-item">
        <svg class="contact-icon" viewBox="0 0 24 24"><circle cx="12" cy="12" r="12" fill="#fff"/><path d="M8.3 6.5l2 2.4-1.2 1.4a8 8 0 0 0 4.6 4.6l1.4-1.2 2.4 2-1.3 1.8c-4.6-.4-8.9-4.7-9.3-9.3z" fill="#2b78b4"/></svg>
        <span>555-013-2748</span>
      </li>
      <li class="contact-item">
        <svg class="contact-icon" viewBox="0 0 24 24"><circle cx="12" cy="12" r="12" fill="#fff"/><rect x="6" y="8" width="12" height="8.5" rx="1" fill="#2b78b4"/><path d="M6.5 8.7L12 13l5.5-4.3" stroke="#fff" stroke-width="1.2" fill="none"/></svg>
        <span>marcus@rt-garland.example</span>
      </li>
      <li class="contact-item">
        <svg class="contact-icon" viewBox="0 0 24 24"><circle cx="12" cy="12" r="12" fill="#fff"/><circle cx="12" cy="12" r="6" fill="none" stroke="#2b78b4" stroke-width="1.4"/><ellipse cx="12" cy="12" rx="2.6" ry="6" fill="none" stroke="#2b78b4" stroke-width="1.2"/><path d="M6 12h12" stroke="#2b78b4" stroke-width="1.2"/></svg>
        <span>www.rt-garland.example</span>
      </li>
    </ul>
  </article>
</main>
</body>
</html>
```